Sales presentation introduction for Finance and Tech firms

Our business is two fold - 1) recruitment 2) consultancy. We would like a one or two page template that we can use to send to potential clients. The template will ideally be the same for the recruitment and consultancy side. We need to be able to edit the template to enter text.

I have attached our logo so you can see what we currently use on Quellbrook.

Sector is financial services and technology. We do not intent to have lots of text but the layout/images/designs to be used should cover some of page in a way that it takes up some space to avoid having to write lot of text.

Open to colour suggestions.

Please look at the attached word doc to see the text I would like for the two presentations.

Happy to answer questions.

Target Market(s)

Directors

Industry/Entity Type

Finance and tech companies

Colors
0094D4
00A9DD
6FCCEA
C7EBF8
E9F6FB

Requirements
Must have
• Editable text

```html
<!DOCTYPE html>
<html lang="en">
<head>
<meta charset="utf-8">
<title>Veranta – We Are Hiring Flyer</title>
<link rel="stylesheet" href="https://fonts.googleapis.com/css2?family=Montserrat:wght@400;500;700&family=Roboto:wght@400;500&family=Roboto+Condensed:wght@400&display=swap">
<style>
  :root {
    --page-bg: #e9f6fb;
    --paper: #ffffff;
    --navy: #1b3a66;
    --royal: #1d5aa7;
    --mid-blue: #2a7fd0;
    --bright-blue: #1f7ac7;
    --sky: #7cc4ec;
    --pale: #c7ebf8;
    --ink: #2b2b2b;
    --body-ink: #333333;
    --logo-grey: #6d6e71;
  }
  * { margin: 0; padding: 0; box-sizing: border-box; }
  html, body { width: 1200px; height: 1200px; overflow: hidden; background: var(--page-bg); }
  .flyer-stage { position: relative; width: 1200px; height: 1200px; }
  .flyer {
    position: absolute; left: 160px; top: 30px;
    width: 786px; height: 1018px;
    transform: scale(1.12); transform-origin: top left;
    background: var(--paper);
    box-shadow: 0 6px 24px rgba(0, 40, 80, 0.18);
    overflow: hidden;
  }
  .header-art { position: absolute; left: 0; top: 0; width: 786px; height: 402px; }
  .brand {
    position: absolute; left: 54px; top: 150px;
    display: flex; align-items: center; gap: 10px;
    font-family: 'Montserrat', sans-serif; font-weight: 400;
    font-size: 34px; letter-spacing: 1px; color: var(--logo-grey);
  }
  .brand-mark { width: 18px; height: 18px; background: var(--royal); }
  .band-text { position: absolute; color: #fff; font-family: 'Roboto Condensed', sans-serif; }
  .band-text.target { left: 42px; top: 289px; width: 360px; }
  .band-text.target h2 { font-weight: 400; font-size: 22px; letter-spacing: 0.2px; margin-bottom: 6px; }
  .band-text.target p { font-size: 13px; line-height: 17px; }
  .band-text.hiring { left: 494px; top: 279px; width: 280px; }
  .band-text.hiring h2 { font-weight: 400; font-size: 33px; margin-bottom: 4px; }
  .band-text.hiring p { font-size: 13px; line-height: 17px; text-align: center; width: 255px; }

  .intro-title {
    position: absolute; left: 44px; top: 420px; width: 280px;
    font-family: 'Montserrat', sans-serif; font-weight: 700;
    font-size: 27px; line-height: 34px; color: var(--ink);
  }
  .intro-rule { position: absolute; left: 335px; top: 427px; width: 2px; height: 62px; background: var(--sky); }
  .copy {
    position: absolute; font-family: 'Roboto', sans-serif;
    font-size: 14.5px; line-height: 23px; color: var(--body-ink);
  }
  .copy.intro { left: 370px; top: 425px; width: 380px; }
  .copy.side { left: 370px; top: 556px; width: 378px; text-align: justify; }
  .copy.side p + p { margin-top: 23px; }
  .copy.wide { left: 47px; top: 823px; width: 700px; text-align: justify; }
  .section-title {
    position: absolute; font-family: 'Roboto', sans-serif; font-weight: 400;
    font-size: 28px; color: var(--ink);
  }
  .section-title.side { left: 372px; top: 518px; }
  .section-title.wide { left: 47px; top: 780px; }
  .team-photo {
    position: absolute; left: 45px; top: 522px; width: 293px; height: 236px;
    border: 13px solid var(--bright-blue);
    background: linear-gradient(135deg, #eef2f6 0%, #c9d3de 45%, #3a4a66 75%, #1f2a3d 100%);
  }
  .tagline {
    position: absolute; left: 44px; top: 911px;
    font-family: 'Montserrat', sans-serif; font-weight: 700;
    font-size: 19px; color: var(--ink);
  }
  .footer-art { position: absolute; left: 0; top: 947px; width: 786px; height: 46px; }
  .footer-address {
    position: absolute; left: 44px; top: 959px;
    font-family: 'Montserrat', sans-serif; font-size: 17px; color: #fff;
  }
  .footer-contact {
    position: absolute; left: 562px; top: 957px;
    font-family: 'Montserrat', sans-serif; font-size: 11.5px; line-height: 14px; color: #fff;
  }
</style>
</head>
<body>
<div class="flyer-stage">
  <article class="flyer">
    <svg class="header-art" viewBox="0 0 786 402" xmlns="http://www.w3.org/2000/svg">
      <g role="img" aria-label="Photo of job candidates seated in a row holding folders while waiting for interviews">
        <defs>
          <linearGradient id="candidatesTone" x1="0" y1="0" x2="0" y2="1">
            <stop offset="0" stop-color="#c9c4bd"/>
            <stop offset="0.55" stop-color="#8a7a6c"/>
            <stop offset="1" stop-color="#d8d6d2"/>
          </linearGradient>
        </defs>
        <polygon points="272,0 786,0 786,385 500,385" fill="url(#candidatesTone)"/>
      </g>
      <polygon points="250,0 274,0 502,385 478,385" fill="var(--royal)"/>
      <polygon points="196,267 340,135 352,267" fill="var(--sky)"/>
      <polygon points="228,267 352,152 432,267" fill="var(--mid-blue)"/>
      <polygon points="0,267 390,267 451,371 0,371" fill="var(--navy)"/>
      <polygon points="392,267 456,267 500,371 452,371" fill="var(--mid-blue)"/>
      <polygon points="455,267 786,267 786,371 500,371" fill="var(--royal)"/>
      <polygon points="78,385 92,371 130,371 116,385" fill="var(--sky)"/>
      <rect x="0" y="384" width="786" height="17" fill="var(--sky)"/>
    </svg>

    <div class="brand"><span class="brand-mark"></span>VERANTA</div>

    <div class="band-text target">
      <h2>TARGET THE RIGHT CANDIDATES</h2>
      <p>Trying to find an employee that will not only fit with the job you are hiring for but also your company culture can be a challenge.</p>
    </div>
    <div class="band-text hiring">
      <h2>WE ARE HIRING</h2>
      <p>ARE YOU A GRADUATE OR UNDERGRADUATE WITH PRIOR BPO EXPERIENCE?</p>
    </div>

    <h1 class="intro-title">We Help Business Grow Effeciently</h1>
    <div class="intro-rule"></div>
    <p class="copy intro">Job seekers use social media to research companies and learn about new job opportunities. Use this example of 'We're hiring' social media post to create</p>

    <div class="team-photo" role="img" aria-label="Photo of three young professionals reviewing documents on a clipboard at a desk"></div>

    <h3 class="section-title side">Job seekers</h3>
    <div class="copy side">
      <p>Job seekers use social media to research companies and learn about new job opportunities. Use this example of 'We're hiring' social media post to create Job seekers use social media to research companies and learn about new job opportunities.</p>
      <p>Use this example of 'We're hiring' social media post to create Job seekers use social media to research companies and learn about new job opportunities.</p>
    </div>

    <h3 class="section-title wide">Job seekers</h3>
    <p class="copy wide">Job seekers use social media to research companies and learn about new job opportunities. Use this example of 'We're hiring' social media post to create Job seekers use social media to research companies and learn about new job opportunities.</p>

    <p class="tagline">We Help Business Grow Effeciently</p>

    <svg class="footer-art" viewBox="0 0 786 46" xmlns="http://www.w3.org/2000/svg">
      <polygon points="0,0 418,0 446,46 0,46" fill="var(--navy)"/>
      <polygon points="432,0 450,0 478,46 460,46" fill="var(--pale)"/>
      <polygon points="454,0 478,0 506,46 482,46" fill="#aeb8dc"/>
      <polygon points="482,0 786,0 786,46 510,46" fill="var(--royal)"/>
    </svg>
    <p class="footer-address">42 Harborfield Road Boston, MA 02118</p>
    <p class="footer-contact">hello@veranta-hire.com<br>www.veranta-hire.com</p>
  </article>
</div>
</body>
</html>
```